Business Card Design

I need a business card design for a photography business that specializes in headshots and portraits.

Target Market(s)

Business professionals, actors, actresses

Industry/Entity Type

Business

Contact Information for Business Card

Cobalt Ridge Photography, Greg Whitlow, 5817 Kellerman Ave, Suite 416, Fort Wayne, IN 46915, 260.555.0187, www.cobaltridgephoto.example. greg.whitlow@cobaltridgephoto.example

Requirements
Must have
• The business card should state the type of photography services offered: headshots and portraits.

```html
<!DOCTYPE html>
<html lang="en">
<head>
<meta charset="utf-8">
<title>Cobalt Ridge Photography – Business Card</title>
<link rel="stylesheet" href="https://fonts.googleapis.com/css2?family=Cinzel:wght@400;500&display=swap">
<style>
  :root {
    --paper: #ffffff;
    --band: #2a2a2a;
    --band-edge: #9a9a9a;
    --ink: #1a1a1a;
    --ink-soft: #6a6a6a;
    --portrait-top: #5a5a5a;
    --portrait-bottom: #b8b8b8;
    --url-ink: #f4f4f4;
  }
  html, body {
    margin: 0;
    padding: 0;
    overflow: hidden;
    background: var(--paper);
  }
  .card {
    position: relative;
    width: 1200px;
    height: 702px;
    background: var(--paper);
    overflow: hidden;
    font-family: "Cinzel", "Times New Roman", serif;
  }
  .band-vertical {
    position: absolute;
    left: 783px;
    top: 0;
    width: 157px;
    height: 702px;
    background: linear-gradient(90deg, var(--paper) 0%, var(--band-edge) 4%, var(--band) 9%, var(--band) 91%, var(--band-edge) 96%, var(--paper) 100%);
  }
  .band-horizontal {
    position: absolute;
    left: 0;
    top: 359px;
    width: 1200px;
    height: 111px;
    background: linear-gradient(180deg, var(--paper) 0%, var(--band-edge) 12%, var(--band) 16%, var(--band) 84%, var(--band-edge) 88%, var(--paper) 100%);
  }
  .portrait {
    position: absolute;
    left: 581px;
    top: 86px;
    width: 542px;
    height: 572px;
    background: linear-gradient(180deg, var(--portrait-top) 0%, var(--portrait-bottom) 100%);
  }
  .brand {
    position: absolute;
    left: 40px;
    top: 62px;
    width: 570px;
    margin: 0;
    text-align: center;
    font-weight: 400;
    line-height: 1;
  }
  .brand-line-top {
    display: block;
    font-size: 58px;
    background: linear-gradient(180deg, #9a9a9a, #555555);
    -webkit-background-clip: text;
    background-clip: text;
    -webkit-text-fill-color: transparent;
  }
  .brand-line-main {
    display: block;
    margin-top: 18px;
    font-size: 60px;
    color: var(--ink);
  }
  .owner {
    position: absolute;
    left: 40px;
    top: 260px;
    width: 570px;
    margin: 0;
    text-align: center;
    font-size: 48px;
    font-weight: 400;
    line-height: 1;
    background: linear-gradient(180deg, #9a9a9a 0%, #111111 70%);
    -webkit-background-clip: text;
    background-clip: text;
    -webkit-text-fill-color: transparent;
  }
  .swoosh {
    position: absolute;
    left: 149px;
    top: 308px;
    width: 421px;
    height: 40px;
  }
  .website {
    position: absolute;
    left: 94px;
    top: 399px;
    margin: 0;
    font-size: 32px;
    font-weight: 500;
    color: var(--url-ink);
    text-shadow: 2px 3px 3px rgba(0,0,0,0.9);
    text-transform: uppercase;
    line-height: 1;
  }
  .contact {
    position: absolute;
    left: 80px;
    top: 505px;
    margin: 0;
    font-style: normal;
    font-size: 27px;
    line-height: 39px;
    color: var(--ink);
    display: grid;
    grid-template-columns: 277px auto;
  }
  .services {
    position: absolute;
    left: 80px;
    top: 635px;
    margin: 0;
    font-size: 22px;
    letter-spacing: 1px;
    color: var(--ink-soft);
    line-height: 1;
  }
</style>
</head>
<body>
  <div class="card">
    <div class="band-horizontal"></div>
    <div class="band-vertical"></div>

    <div class="portrait" role="img" aria-label="Illustrated portrait of a woman in a strapless gown, set over the crossing bands"></div>

    <h1 class="brand">
      <span class="brand-line-top">Cobalt Ridge</span>
      <span class="brand-line-main">Photography</span>
    </h1>

    <p class="owner">Greg Whitlow</p>
    <svg class="swoosh" viewBox="0 0 421 40" aria-hidden="true">
      <path d="M0 36 Q210 34 416 2 Q220 30 0 36 Z" fill="#b8b8b8"/>
    </svg>

    <p class="website">www.cobaltridgephoto.example</p>

    <address class="contact">
      <span>5817 Kellerman Ave</span><span>Suite 416</span>
      <span>Fort Wayne, IN</span><span>46915</span>
      <span>260.555.0187</span><span></span>
    </address>

    <p class="services">Headshots &amp; Portraits</p>
  </div>
</body>
</html>
```